Business Card Design for Corvella

Need a business card designed for Corvella employees.
- 2 sided business card
- Front:
Company Logo (file attached)
Background could be:white with perhaps a red/black stripe on the left
OR
Background could be: OR dark red-black gradient: be creative
Include the following on the front:
Marcus Dellow
Founder & CEO
marcus.dellow@corvella-example.com
+1 555.010.0147
corvella-example.com
- Back: White color background with company logo
Text under the logo: Invoice Automation 2.0
** be creative about the font, mix of upper and lower case and colors for the text **
Target Market(s)
We are a software company marketing our products to large and medium sized businesses.
Industry/Entity Type
Business

```html
<!DOCTYPE html>
<html lang="en">
<head>
<meta charset="utf-8">
<title>Corvella Business Card</title>
<link rel="stylesheet" href="https://fonts.googleapis.com/css2?family=Arimo:wght@700&family=Open+Sans:wght@600;700&family=Pinyon+Script&display=swap">
<style>
  :root {
    --page-bg: #ffffff;
    --card-red-light: #c12a2c;
    --card-red: #a02428;
    --card-red-dark: #6b2121;
    --card-text: #ffffff;
    --brand-light: #e3e3e3;
    --brand-dark: #3a3a3a;
    --mark-orange: #d9651a;
    --tagline: #6e1518;
  }
  html, body {
    margin: 0;
    padding: 0;
    width: 1000px;
    height: 1200px;
    overflow: hidden;
    background: var(--page-bg);
  }
  .canvas {
    position: relative;
    width: 1000px;
    height: 1200px;
  }
  .card-front {
    position: absolute;
    left: 120px;
    top: 190px;
    width: 721px;
    height: 417px;
    background:
      linear-gradient(135deg, var(--card-red-light) 0%, var(--card-red) 35%, var(--card-red-dark) 100%);
    overflow: hidden;
  }
  .brand {
    position: absolute;
    display: flex;
    align-items: center;
  }
  .brand-mark {
    border-radius: 50%;
    background: var(--mark-orange);
    flex: none;
  }
  .brand-name {
    font-family: "Open Sans", sans-serif;
    font-weight: 600;
    letter-spacing: 0.04em;
    text-transform: uppercase;
    line-height: 1;
  }
  .card-front .brand {
    left: 56px;
    top: 52px;
  }
  .card-front .brand-mark {
    width: 68px;
    height: 68px;
    margin-right: 14px;
  }
  .card-front .brand-name {
    font-size: 42px;
    color: var(--brand-light);
  }
  .person {
    position: absolute;
    left: 424px;
    top: 142px;
    color: var(--card-text);
    font-family: "Arimo", sans-serif;
    font-weight: 700;
  }
  .person-name {
    font-size: 26px;
    margin: 0;
    line-height: 1.2;
  }
  .person-title {
    font-size: 20px;
    margin: 2px 0 0;
    line-height: 1.2;
  }
  .contact {
    position: absolute;
    left: 84px;
    top: 278px;
    margin: 0;
    color: var(--card-text);
    font-family: "Open Sans", sans-serif;
    font-weight: 700;
    font-size: 21px;
    line-height: 31px;
    display: grid;
    grid-template-columns: 70px auto;
  }
  .contact dt, .contact dd { margin: 0; }
  .card-back {
    position: absolute;
    left: 0;
    top: 700px;
    width: 1000px;
    height: 260px;
  }
  .card-back .brand {
    left: 192px;
    top: 36px;
  }
  .card-back .brand-mark {
    width: 130px;
    height: 130px;
    margin-right: 26px;
  }
  .card-back .brand-name {
    font-size: 76px;
    color: var(--brand-dark);
  }
  .tagline {
    position: absolute;
    left: 370px;
    top: 166px;
    margin: 0;
    font-family: "Pinyon Script", cursive;
    font-size: 32px;
    color: var(--tagline);
    letter-spacing: 0.02em;
  }
</style>
</head>
<body>
<main class="canvas">
  <section class="card-front" aria-label="Business card front">
    <div class="brand">
      <span class="brand-mark"></span>
      <span class="brand-name">Corvella</span>
    </div>
    <div class="person">
      <p class="person-name">Marcus Dellow</p>
      <p class="person-title">Founder &amp; CEO</p>
    </div>
    <dl class="contact">
      <dt>E-mail</dt><dd>: marcus.dellow@corvella-example.com</dd>
      <dt>Tel</dt><dd>: +1 555.010.0147</dd>
      <dt>Web</dt><dd>: corvella-example.com</dd>
    </dl>
  </section>

  <section class="card-back" aria-label="Business card back">
    <div class="brand">
      <span class="brand-mark"></span>
      <span class="brand-name">Corvella</span>
    </div>
    <p class="tagline">Invoice Automation 2.0</p>
  </section>
</main>
</body>
</html>
```